VelloTrack/Plivex: map and navigation, GIS, ICT, B2B, technology, IT projects

Company profile: Tech company, national leader (Poland) in mapping and car nav solutions. The main brand is VelloTrack for which we recently had a logo lift. Plivex is the brand of business GIS products and we present it as "Plivex by VelloTrack".

Attachements:
- VelloTrack logo,
- VelloTrack application icon,
- Plivex by VelloTrack logo,
- VelloTrack LogoGuide with approved colors,
- few sample slides,
- link to Polish regions: https://lnk.example-short.net/Qw7rT2
- link to our www: vellotrack.pl & plivex.pl

Target Market(s)

We focus on the domestic market. Our main B2B customers are international companies operating on the Polish market.

Font styles to use
Serif
Sans Serif
Other font styles liked:
• Lato, Artegra_Sans

Colors
0455a3
3176b5
85abd2
9bcb3b

Requirements
Must have
• Expectations: consistency of graphic layout of all presentation templates (business, portfolio, advertising, etc.). The color scheme should be consistent with our brands. We expect colors, style, fonts, layouts and a set of icons in the project. For stock photos please use stockframe-images.com.
• Expected stylistics: elegant, technological, business, modern. Please note that the proposed fonts should contain polish characters (ą ę ł ś ć ż ź ó).
• We expect a dozen or so templates of slides. Among them should be:
• - Title + midpage title,
• - Table of contents / agenda,
• - Slide: 2-3 graphics + text,
• - Slide: only graphics (4-8),
• - Slide: typical for the portfolio (clients' logos, graphics, text),
• - Slide: timeline + project milestones overview,
• - Slide with the offer and prices with description
• - (!) Some creative ideas for infographics related to maps,
• - Couple of structure and proccess SmartArt,
• - "Contact us" slide

```html
<!DOCTYPE html>
<html lang="en">
<head>
<meta charset="utf-8">
<title>Plivex by VelloTrack – Presentation Template</title>
<link href="https://fonts.googleapis.com/css2?family=Lato:wght@300;400;700;900&display=swap" rel="stylesheet">
<style>
:root{
  --navy:#1d2b5c;--navy-deep:#15214a;--green:#4a7c22;--green-2:#5a8a2e;--green-3:#6c9a3a;--green-4:#7ea84e;
  --red:#b1363f;--yellow:#e6bf45;--blue:#3176b5;--sky:#5b8fd0;--lime:#9bcb3b;
  --ink:#222;--text:#5d5d5d;--band:#efefef;--khaki:#8b8262;--line:#dcdcdc;
  --ph-traffic:linear-gradient(135deg,#2b3550 0%,#4d4656 40%,#a5563f 68%,#2a3048 100%);
  --ph-road:linear-gradient(160deg,#243562 0%,#3f5282 45%,#8e7060 72%,#1b2646 100%);
  --ph-car:linear-gradient(120deg,#9aa5ad 0%,#3d4650 50%,#6f7a82 100%);
  --ph-bluecar:linear-gradient(170deg,#9fb2c6 0%,#2e5fb0 60%,#44494f 100%);
  --ph-city:linear-gradient(180deg,#e4e4e4 0%,#bdbdbd 100%);
  --ph-person:linear-gradient(180deg,#cfd3d8 0%,#8a9099 100%);
  --ph-map:linear-gradient(135deg,#e9ecf2 0%,#c9cfdc 55%,#7d8bb0 100%);
  --ph-hand:linear-gradient(170deg,#f4f4f4 0%,#dcdcdc 45%,#c9ab92 100%);
}
*{box-sizing:border-box}
html,body{margin:0;width:1200px;height:2280px;overflow:hidden;background:#fff}
body{font-family:'Lato',sans-serif;color:var(--ink)}
p,h1,h2,h3,h4{margin:0}
.deck{display:grid;grid-template-columns:repeat(3,388px);grid-auto-rows:220px;column-gap:12px;row-gap:33px;padding:15px 6px 0}
.slide{position:relative;overflow:hidden;background:#fff;box-shadow:0 1px 3px rgba(0,0,0,.2)}
.a{position:absolute}
.navy-bg{background:var(--navy)}
.photo{position:absolute;background:var(--ph-traffic)}
.photo.road{background:var(--ph-road)}
.photo.car{background:var(--ph-car)}
.photo.bluecar{background:var(--ph-bluecar)}
.photo.city{background:var(--ph-city)}
.photo.person{background:var(--ph-person)}
.photo.map{background:var(--ph-map)}
.photo.hand{background:var(--ph-hand)}
.shade{position:absolute;inset:0;background:linear-gradient(90deg,rgba(21,33,74,.55),rgba(21,33,74,.25))}

.head{position:absolute;left:0;top:0;right:0;height:30px;background:var(--band)}
.head h2{position:absolute;left:10px;top:9px;font-size:11px;font-weight:700;color:var(--ink)}
.head h2::after{content:"";position:absolute;left:0;top:17px;width:18px;height:2px;background:var(--green)}
.brand{position:absolute;right:10px;top:10px;font-size:9px;font-weight:900;color:var(--navy)}
.foot{position:absolute;left:10px;bottom:6px;font-size:4px;color:#999}
.pg{position:absolute;right:10px;bottom:6px;font-size:4px;color:#999}

.logo{display:flex;align-items:center;gap:6px}
.logo-mark{display:block;background:var(--lime)}
.logo-name{font-weight:900;color:#fff;letter-spacing:-.5px}
.logo-by{font-weight:900;color:#fff}

.t{font-size:4.6px;line-height:1.5;color:var(--text)}
.t.w{color:rgba(255,255,255,.85)}
.h{font-size:7px;font-weight:700;color:var(--ink)}
.h.w{color:#fff}
.ic{display:flex;align-items:center;justify-content:center;border-radius:50%;background:var(--green)}
.ic svg{width:55%;height:55%}
.ic.navy{background:var(--navy)}
.ic.red{background:var(--red)}
.ic.yellow{background:var(--yellow)}
.ic.ring{background:transparent;border:1.5px solid #fff}
.row{display:flex;gap:6px;align-items:flex-start}
.num{color:#fff;font-size:6px;font-weight:700}
.tile{position:absolute;padding:10px;color:#fff;text-align:center}
.price{font-size:22px;font-weight:900;color:#fff;line-height:1}
.price small{font-size:6px;font-weight:400}
.btn{display:inline-block;margin-top:8px;padding:3px 12px;border-radius:8px;font-size:4.5px;color:#fff;border:1px solid rgba(255,255,255,.6)}
table{border-collapse:collapse;width:100%}
.data td,.data th{font-size:4.6px;padding:2.6px 6px;text-align:center;color:#444}
.data th{background:var(--navy);color:#fff;font-weight:700}
.data tr:nth-child(even) td{background:#f1f2f5}
.data td:first-child,.data th:first-child{text-align:left}
.cat{font-size:7px;font-weight:700}
.tab-ic{display:inline-block;width:5px;height:5px;background:var(--navy);margin-right:3px;vertical-align:middle}
</style>
</head>
<body>
<main class="deck">

<!-- 1 cover -->
<section class="slide navy-bg">
  <div class="a logo" style="left:62px;top:80px"><span class="logo-mark" style="width:14px;height:14px"></span><span class="logo-name" style="font-size:40px">Plivex</span></div>
  <p class="a logo-by" style="left:190px;top:128px;font-size:9px">by VelloTrack</p>
</section>

<!-- 2 title -->
<section class="slide navy-bg" style="text-align:center">
  <div class="a logo" style="left:0;right:0;top:48px;justify-content:center"><span class="logo-mark" style="width:7px;height:7px"></span><span class="logo-name" style="font-size:18px">Plivex</span></div>
  <p class="a logo-by" style="left:0;right:0;top:72px;font-size:5px">by VelloTrack</p>
  <h1 class="a" style="left:0;right:0;top:92px;font-size:22px;font-weight:900;color:#fff">Your Title Here</h1>
  <p class="a" style="left:0;right:0;top:122px;font-size:6px;font-weight:700;color:#fff">Your Subtitle Goes Here</p>
</section>

<!-- 3 title with photo -->
<section class="slide">
  <div class="photo road" style="inset:0" role="img" aria-label="Long-exposure photo of evening highway traffic"></div>
  <div class="shade"></div>
  <div class="a" style="left:118px;top:62px;text-align:center;width:200px">
    <div class="logo" style="justify-content:center"><span class="logo-mark" style="width:7px;height:7px"></span><span class="logo-name" style="font-size:18px">Plivex</span></div>
    <p class="logo-by" style="font-size:5px;margin-top:2px">by VelloTrack</p>
    <h1 style="font-size:22px;font-weight:900;color:#fff;margin-top:6px">Your Title Here</h1>
    <p style="font-size:6px;font-weight:700;color:#fff;margin-top:2px">Your Subtitle Goes Here</p>
  </div>
  <p class="a" style="left:168px;bottom:14px;font-size:5px;color:#fff">www.yourwebsite.com</p>
</section>

<!-- 4 about us -->
<section class="slide">
  <div class="head"><h2>About Us</h2><span class="brand">VelloTrack</span></div>
  <div class="a" style="left:10px;right:10px;top:44px">
    <p class="t">Contrary to popular belief, Lorem Ipsum is not simply random text. It has roots in a piece of classical Latin literature from 45 BC, making it over 2000 years old. A professor at a small college looked up one of the more obscure Latin words, consectetur, from a Lorem Ipsum passage, and going through the cites of the word in classical literature, discovered the undoubtable source. It comes from sections of a treatise on the theory of ethics, very popular during the Renaissance.</p>
    <p class="t" style="margin-top:6px">Contrary to popular belief, Lorem Ipsum is not simply random text. It has roots in a piece of classical Latin literature from 45 BC, making it over 2000 years old. A professor at a small college looked up one of the more obscure Latin words, consectetur, from a Lorem Ipsum passage, and going through the cites of the word in classical literature, discovered the undoubtable source. The first line of Lorem Ipsum comes from a line in section 1.10.32.</p>
    <p class="t" style="margin-top:6px">Contrary to popular belief, Lorem Ipsum is not simply random text. It has roots in a piece of classical Latin literature from 45 BC, making it over 2000 years old. It comes from sections of a treatise on the theory of ethics, very popular during the Renaissance. The first line comes from a line in section 1.10.32 of the book.</p>
  </div>
  <p class="foot">© Copyright 2019 Plivex by VelloTrack. All rights reserved.</p><span class="pg">4</span>
</section>

<!-- 5 agenda -->
<section class="slide">
  <div class="head"><h2>Our Agenda</h2><span class="brand">VelloTrack</span></div>
  <div class="a" style="left:30px;top:48px;display:grid;grid-template-columns:170px 170px;row-gap:22px">
    <div class="row"><span class="ic navy" style="width:18px;height:18px;flex:none"><span class="num">01</span></span><div><p class="h">Agenda One</p><p class="t">Lorem ipsum dolor sit amet, consectetur adipiscing elit, sed do eiusmod tempor.</p></div></div>
    <div class="row"><span class="ic navy" style="width:18px;height:18px;flex:none"><span class="num">04</span></span><div><p class="h">Agenda Four</p><p class="t">Lorem ipsum dolor sit amet, consectetur adipiscing elit, sed do eiusmod tempor.</p></div></div>
    <div class="row"><span class="ic navy" style="width:18px;height:18px;flex:none"><span class="num">02</span></span><div><p class="h">Agenda Two</p><p class="t">Lorem ipsum dolor sit amet, consectetur adipiscing elit, sed do eiusmod tempor.</p></div></div>
    <div class="row"><span class="ic navy" style="width:18px;height:18px;flex:none"><span class="num">05</span></span><div><p class="h">Agenda Five</p><p class="t">Lorem ipsum dolor sit amet, consectetur adipiscing elit, sed do eiusmod tempor.</p></div></div>
    <div class="row"><span class="ic navy" style="width:18px;height:18px;flex:none"><span class="num">03</span></span><div><p class="h">Agenda Three</p><p class="t">Lorem ipsum dolor sit amet, consectetur adipiscing elit, sed do eiusmod tempor.</p></div></div>
    <div class="row"><span class="ic navy" style="width:18px;height:18px;flex:none"><span class="num">06</span></span><div><p class="h">Agenda Six</p><p class="t">Lorem ipsum dolor sit amet, consectetur adipiscing elit, sed do eiusmod tempor.</p></div></div>
  </div>
  <p class="foot">© Copyright 2019 Plivex by VelloTrack. All rights reserved.</p><span class="pg">5</span>
</section>

<!-- 6 market overview -->
<section class="slide">
  <div class="head"><h2>Market Overview</h2><span class="brand">VelloTrack</span></div>
  <div class="a navy-bg" style="left:10px;top:40px;width:80px;height:72px;padding:6px">
    <span class="ic ring" style="width:12px;height:12px"><svg viewBox="0 0 12 12"><path d="M3 6l2 2 4-5" stroke="#fff" stroke-width="1.6" fill="none"/></svg></span>
    <p class="h w" style="margin-top:3px">Heading Text</p>
    <p class="t w">Lorem ipsum dolor sit amet, consectetur adipiscing elit sed do eiusmod.</p>
  </div>
  <div class="a" style="left:10px;top:118px;width:80px">
    <span class="ic navy" style="width:12px;height:12px"><svg viewBox="0 0 12 12"><path d="M3 6l2 2 4-5" stroke="#fff" stroke-width="1.6" fill="none"/></svg></span>
    <p class="h" style="margin-top:3px">Heading Text</p>
    <p class="t">Lorem ipsum dolor sit amet, consectetur adipiscing elit sed do eiusmod.</p>
  </div>
  <div class="photo" style="left:95px;top:40px;width:100px;height:72px" role="img" aria-label="Photo of a congested multi-lane road"></div>
  <div class="a navy-bg" style="left:195px;top:40px;width:183px;height:72px"></div>
  <svg class="a" style="left:210px;top:48px" width="56" height="56" viewBox="0 0 56 56">
    <circle cx="28" cy="28" r="23" fill="#fff"/>
    <circle cx="28" cy="28" r="23" fill="none" stroke="#3a4670" stroke-width="5"/>
    <circle cx="28" cy="28" r="23" fill="none" stroke="var(--yellow)" stroke-width="5" stroke-dasharray="86.7 144.5" transform="rotate(-90 28 28)"/>
    <text x="28" y="32" text-anchor="middle" font-family="Lato,sans-serif" font-size="11" font-weight="900" fill="var(--navy)">60%</text>
  </svg>
  <div class="a" style="left:290px;top:44px;width:82px">
    <p class="h w">Heading Text</p><p class="t w">Lorem ipsum dolor sit amet, consectetur adipiscing elit.</p>
    <p class="h w" style="margin-top:6px">Heading Text</p><p class="t w">Lorem ipsum dolor sit amet, consectetur adipiscing elit.</p>
  </div>
  <div class="a" style="left:100px;top:120px;right:10px">
    <p class="h">Heading Text</p>
    <p class="t">Lorem ipsum dolor sit amet, consectetur adipiscing elit, sed do eiusmod tempor incididunt ut labore et dolore magna aliqua. Ut enim ad minim veniam, quis nostrud exercitation ullamco laboris nisi ut aliquip ex ea commodo consequat. Duis aute irure dolor in reprehenderit in voluptate velit esse cillum dolore eu fugiat nulla pariatur.</p>
  </div>
  <p class="foot">© Copyright 2019 Plivex by VelloTrack. All rights reserved.</p><span class="pg">6</span>
</section>

<!-- 7 mockup picture -->
<section class="slide">
  <div class="a" style="left:22px;top:48px;width:118px;height:78px;background:#222;border-radius:3px;padding:4px">
    <div class="photo" style="position:relative;width:100%;height:100%" role="img" aria-label="Monitor screen showing a traffic jam photo"></div>
  </div>
  <div class="a" style="left:70px;top:126px;width:22px;height:12px;background:#bbb"></div>
  <div class="a" style="left:60px;top:138px;width:42px;height:3px;background:#aaa;border-radius:2px"></div>
  <div class="a navy-bg" style="left:225px;top:0;width:135px;height:195px;padding:40px 14px 0">
    <h3 style="font-size:14px;font-weight:300;color:#fff;line-height:1.2">Awesome Mockup Picture</h3>
    <p class="t w" style="margin-top:12px;font-weight:700">At vero eos et accusamus et iusto odio dignissimos ducimus qui blanditiis praesentium voluptatum deleniti atque corrupti quos dolores et quas molestias excepturi.</p>
  </div>
</section>

<!-- 8 double smartphones -->
<section class="slide">
  <div class="head"><h2>Double Smartphones Mockup</h2><span class="brand">VelloTrack</span></div>
  <svg class="a" style="left:0;top:0" width="388" height="220"><polygon points="200,220 388,220 388,82" fill="var(--green)"/></svg>
  <p class="a t" style="left:12px;top:42px;width:180px">At vero eos et accusamus et iusto odio dignissimos ducimus qui blanditiis praesentium voluptatum deleniti.</p>
  <div class="a" style="left:12px;top:62px;width:180px;display:grid;row-gap:9px">
    <div class="row"><span class="ic" style="width:12px;height:12px;flex:none"><svg viewBox="0 0 12 12"><path d="M3 6l2 2 4-5" stroke="#fff" stroke-width="1.6" fill="none"/></svg></span><p class="t">Lorem ipsum dolor sit amet, consectetur adipiscing elit, sed do eiusmod tempor incididunt ut labore.</p></div>
    <div class="row"><span class="ic" style="width:12px;height:12px;flex:none"><svg viewBox="0 0 12 12"><path d="M3 6l2 2 4-5" stroke="#fff" stroke-width="1.6" fill="none"/></svg></span><p class="t">Duis aute irure dolor in reprehenderit in voluptate velit esse cillum dolore.</p></div>
    <div class="row"><span class="ic" style="width:12px;height:12px;flex:none"><svg viewBox="0 0 12 12"><path d="M3 6l2 2 4-5" stroke="#fff" stroke-width="1.6" fill="none"/></svg></span><p class="t">Lorem ipsum dolor sit amet, consectetur adipiscing elit, sed do eiusmod tempor.</p></div>
    <div class="row"><span class="ic" style="width:12px;height:12px;flex:none"><svg viewBox="0 0 12 12"><path d="M3 6l2 2 4-5" stroke="#fff" stroke-width="1.6" fill="none"/></svg></span><p class="t">Duis aute irure dolor in reprehenderit in voluptate velit esse cillum dolore.</p></div>
  </div>
  <div class="photo" style="left:212px;top:40px;width:48px;height:98px;border-radius:7px;border:3px solid #eee" role="img" aria-label="Smartphone displaying a night traffic photo"></div>
  <div class="photo" style="left:266px;top:50px;width:48px;height:98px;border-radius:7px;border:3px solid #eee" role="img" aria-label="Smartphone displaying a car tail lights photo"></div>
  <p class="foot">© Copyright 2019 Plivex by VelloTrack. All rights reserved.</p><span class="pg">8</span>
</section>

<!-- 9 four color boxes -->
<section class="slide">
  <div class="head"><h2>Your Title Here</h2><span class="brand">VelloTrack</span></div>
  <div class="a navy-bg" style="left:0;right:0;top:60px;height:118px"></div>
  <div class="tile" style="left:10px;top:60px;width:90px;height:118px;background:var(--navy)"><span class="ic ring" style="width:16px;height:16px;margin:0 auto"><svg viewBox="0 0 12 12"><path d="M3 6l2 2 4-5" stroke="#fff" stroke-width="1.6" fill="none"/></svg></span><p class="h w" style="margin:5px 0 3px">Heading Here</p><p class="t w" style="text-align:left">Lorem ipsum dolor sit amet, consectetur adipiscing elit, sed do eiusmod tempor incididunt ut labore et dolore magna aliqua.</p></div>
  <div class="tile" style="left:102px;top:60px;width:90px;height:118px;background:var(--green)"><span class="ic ring" style="width:16px;height:16px;margin:0 auto"><svg viewBox="0 0 12 12"><path d="M3 6l2 2 4-5" stroke="#fff" stroke-width="1.6" fill="none"/></svg></span><p class="h w" style="margin:5px 0 3px">Heading Here</p><p class="t w" style="text-align:left">Lorem ipsum dolor sit amet, consectetur adipiscing elit, sed do eiusmod tempor incididunt ut labore et dolore magna aliqua.</p></div>
  <div class="tile" style="left:194px;top:60px;width:90px;height:118px;background:var(--red)"><span class="ic ring" style="width:16px;height:16px;margin:0 auto"><svg viewBox="0 0 12 12"><path d="M3 6l2 2 4-5" stroke="#fff" stroke-width="1.6" fill="none"/></svg></span><p class="h w" style="margin:5px 0 3px">Heading Here</p><p class="t w" style="text-align:left">Lorem ipsum dolor sit amet, consectetur adipiscing elit, sed do eiusmod tempor incididunt ut labore et dolore magna aliqua.</p></div>
  <div class="tile" style="left:286px;top:60px;width:92px;height:118px;background:var(--yellow)"><span class="ic ring" style="width:16px;height:16px;margin:0 auto"><svg viewBox="0 0 12 12"><path d="M3 6l2 2 4-5" stroke="#fff" stroke-width="1.6" fill="none"/></svg></span><p class="h w" style="margin:5px 0 3px">Heading Here</p><p class="t w" style="text-align:left">Lorem ipsum dolor sit amet, consectetur adipiscing elit, sed do eiusmod tempor incididunt ut labore et dolore magna aliqua.</p></div>
  <p class="foot">© Copyright 2019 Plivex by VelloTrack. All rights reserved.</p><span class="pg">9</span>
</section>

<!-- 10 differences -->
<section class="slide">
  <div class="head"><h2>Our Differences</h2><span class="brand">VelloTrack</span></div>
  <div class="a navy-bg" style="left:10px;top:48px;width:368px;height:112px"></div>
  <div class="a" style="left:20px;top:60px;width:165px;display:grid;row-gap:10px">
    <div class="row"><span class="ic" style="width:11px;height:11px;flex:none"><svg viewBox="0 0 12 12"><path d="M3 6l2 2 4-5" stroke="#fff" stroke-width="1.6" fill="none"/></svg></span><p class="t w">Lorem ipsum dolor sit amet, consectetur adipiscing elit, sed do eiusmod tempor incididunt.</p></div>
    <div class="row"><span class="ic" style="width:11px;height:11px;flex:none"><svg viewBox="0 0 12 12"><path d="M3 6l2 2 4-5" stroke="#fff" stroke-width="1.6" fill="none"/></svg></span><p class="t w">Duis aute irure dolor in reprehenderit in voluptate velit esse cillum dolore.</p></div>
    <div class="row"><span class="ic" style="width:11px;height:11px;flex:none"><svg viewBox="0 0 12 12"><path d="M3 6l2 2 4-5" stroke="#fff" stroke-width="1.6" fill="none"/></svg></span><p class="t w">Lorem ipsum dolor sit amet, consectetur adipiscing elit, sed do eiusmod tempor incididunt.</p></div>
    <div class="row"><span class="ic" style="width:11px;height:11px;flex:none"><svg viewBox="0 0 12 12"><path d="M3 6l2 2 4-5" stroke="#fff" stroke-width="1.6" fill="none"/></svg></span><p class="t w">Duis aute irure dolor in reprehenderit in voluptate velit esse cillum dolore.</p></div>
  </div>
  <div class="photo car" style="left:200px;top:58px;width:168px;height:92px" role="img" aria-label="Photo of a dark sedan driving at speed"></div>
  <p class="foot">© Copyright 2019 Plivex by VelloTrack. All rights reserved.</p><span class="pg">10</span>
</section>

<!-- 11 five columns -->
<section class="slide">
  <div class="tile" style="left:0;top:0;width:78px;height:220px;background:var(--green);padding:30px 8px"><span class="ic ring" style="width:20px;height:20px;margin:0 auto"><svg viewBox="0 0 12 12"><path d="M3 6l2 2 4-5" stroke="#fff" stroke-width="1.4" fill="none"/></svg></span><p class="h w" style="margin:50px 0 3px">Heading Here</p><p class="t w" style="text-align:left">Lorem ipsum dolor sit amet, consectetur adipiscing elit, sed do eiusmod tempor incididunt ut labore et dolore magna aliqua.</p></div>
  <div class="tile" style="left:78px;top:0;width:77px;height:220px;background:var(--green-2);padding:30px 8px"><span class="ic ring" style="width:20px;height:20px;margin:0 auto"><svg viewBox="0 0 12 12"><path d="M3 6l2 2 4-5" stroke="#fff" stroke-width="1.4" fill="none"/></svg></span><p class="h w" style="margin:50px 0 3px">Heading Here</p><p class="t w" style="text-align:left">Lorem ipsum dolor sit amet, consectetur adipiscing elit, sed do eiusmod tempor incididunt ut labore et dolore magna aliqua.</p></div>
  <div class="tile" style="left:155px;top:0;width:78px;height:220px;background:var(--green-3);padding:30px 8px"><span class="ic ring" style="width:20px;height:20px;margin:0 auto"><svg viewBox="0 0 12 12"><path d="M3 6l2 2 4-5" stroke="#fff" stroke-width="1.4" fill="none"/></svg></span><p class="h w" style="margin:50px 0 3px">Heading Here</p><p class="t w" style="text-align:left">Lorem ipsum dolor sit amet, consectetur adipiscing elit, sed do eiusmod tempor incididunt ut labore et dolore magna aliqua.</p></div>
  <div class="tile" style="left:233px;top:0;width:77px;height:220px;background:var(--green-4);padding:30px 8px"><span class="ic ring" style="width:20px;height:20px;margin:0 auto"><svg viewBox="0 0 12 12"><path d="M3 6l2 2 4-5" stroke="#fff" stroke-width="1.4" fill="none"/></svg></span><p class="h w" style="margin:50px 0 3px">Heading Here</p><p class="t w" style="text-align:left">Lorem ipsum dolor sit amet, consectetur adipiscing elit, sed do eiusmod tempor incididunt ut labore et dolore magna aliqua.</p></div>
  <div class="tile" style="left:310px;top:0;width:78px;height:220px;background:var(--navy);padding:30px 8px"><span class="ic ring" style="width:20px;height:20px;margin:0 auto"><svg viewBox="0 0 12 12"><path d="M3 6l2 2 4-5" stroke="#fff" stroke-width="1.4" fill="none"/></svg></span><p class="h w" style="margin:50px 0 3px">Heading Here</p><p class="t w" style="text-align:left">Lorem ipsum dolor sit amet, consectetur adipiscing elit, sed do eiusmod tempor incididunt ut labore et dolore magna aliqua.</p></div>
</section>

<!-- 12 tile grid -->
<section class="slide">
  <div class="head"><h2>Your Title Goes Here</h2><span class="brand">VelloTrack</span></div>
  <div class="photo" style="left:10px;top:48px;width:120px;height:70px" role="img" aria-label="Photo of highway traffic at dusk"></div>
  <div class="tile" style="left:134px;top:48px;width:120px;height:70px;background:var(--green);padding-top:14px"><p class="h w">Heading Goes Here</p><p class="t w">Lorem ipsum dolor sit amet, consectetur adipiscing elit sed do eiusmod.</p></div>
  <div class="photo road" style="left:258px;top:48px;width:120px;height:70px" role="img" aria-label="Photo of light trails on a motorway"></div>
  <div class="tile" style="left:10px;top:122px;width:120px;height:70px;background:var(--navy);padding-top:18px"><p class="h w">Heading Goes Here</p><p class="t w">Lorem ipsum dolor sit amet, consectetur adipiscing elit sed do eiusmod.</p></div>
  <div class="photo bluecar" style="left:134px;top:122px;width:120px;height:70px" role="img" aria-label="Photo of a blue compact car"></div>
  <div class="tile" style="left:258px;top:122px;width:120px;height:70px;background:var(--red);padding-top:18px"><p class="h w">Heading Goes Here</p><p class="t w">Lorem ipsum dolor sit amet, consectetur adipiscing elit sed do eiusmod.</p></div>
  <p class="foot">© Copyright 2019 Plivex by VelloTrack. All rights reserved.</p><span class="pg">12</span>
</section>

<!-- 13 about us photo -->
<section class="slide">
  <div class="photo" style="left:0;top:0;width:210px;height:220px" role="img" aria-label="Photo of cars queuing in traffic"></div>
  <div class="a navy-bg" style="left:150px;top:55px;width:212px;height:108px;padding:20px 16px">
    <h3 style="font-size:13px;font-weight:900;color:#fff">ABOUT US</h3>
    <p class="t w" style="margin-top:8px">Lorem ipsum dolor sit amet, consectetur adipiscing elit, sed do eiusmod tempor incididunt ut labore et dolore magna aliqua.</p>
    <p class="t w" style="margin-top:4px">Ut enim ad minim veniam, quis nostrud exercitation ullamco laboris nisi ut aliquip ex ea commodo consequat.</p>
  </div>
</section>

<!-- 14 tab mockup -->
<section class="slide">
  <div class="photo hand" style="left:0;top:0;width:145px;height:220px" role="img" aria-label="Photo of a hand holding a smartphone that shows night traffic"></div>
  <h3 class="a" style="left:160px;top:34px;font-size:12px;font-weight:900;color:var(--navy);line-height:1.15">Special<br>Tab Mockup</h3>
  <div class="a" style="left:160px;top:80px;display:grid;grid-template-columns:105px 105px;row-gap:14px;column-gap:8px">
    <div><p class="h" style="color:var(--navy)"><span class="tab-ic"></span>Real Estate</p><p class="t">Lorem ipsum dolor sit amet, consectetur adipiscing elit sed.</p></div>
    <div><p class="h" style="color:var(--navy)"><span class="tab-ic"></span>Flight Room</p><p class="t">Lorem ipsum dolor sit amet, consectetur adipiscing elit sed.</p></div>
    <div><p class="h" style="color:var(--navy)"><span class="tab-ic"></span>Social Marketing</p><p class="t">Lorem ipsum dolor sit amet, consectetur adipiscing elit sed.</p></div>
    <div><p class="h" style="color:var(--navy)"><span class="tab-ic"></span>Product Sales</p><p class="t">Lorem ipsum dolor sit amet, consectetur adipiscing elit sed.</p></div>
  </div>
</section>

<!-- 15 divider -->
<section class="slide">
  <div class="photo road" style="inset:0" role="img" aria-label="Long-exposure photo of a highway at night"></div>
  <div class="shade"></div>
  <div class="a logo" style="left:26px;top:108px"><span class="logo-mark" style="width:7px;height:7px"></span><span class="logo-name" style="font-size:16px">Plivex</span></div>
  <h1 class="a" style="left:26px;top:130px;font-size:17px;font-weight:900;color:#fff">This Is Your Divider Page</h1>
  <p class="a" style="left:26px;top:153px;font-size:5.5px;font-weight:700;color:#fff">Your Subtitle Goes Here</p>
</section>

<!-- 16 column chart -->
<section class="slide">
  <div class="photo city" style="inset:0" role="img" aria-label="Faded photo of a city skyline"></div>
  <svg class="a" style="left:0;top:0" width="388" height="220" viewBox="0 0 388 220" font-family="Lato,sans-serif">
    <rect x="150" y="26" width="5" height="5" fill="var(--navy)"/><text x="158" y="31" font-size="5" fill="#444">2018</text>
    <rect x="178" y="26" width="5" height="5" fill="var(--green)"/><text x="186" y="31" font-size="5" fill="#444">2019</text>
    <g font-size="6" font-weight="700" fill="#333" text-anchor="middle">
      <rect x="24" y="87" width="24" height="73" fill="var(--navy)"/><text x="36" y="83">400</text>
      <rect x="52" y="68" width="24" height="92" fill="var(--green)"/><text x="64" y="64">500</text>
      <rect x="119" y="105" width="24" height="55" fill="var(--navy)"/><text x="131" y="101">300</text>
      <rect x="147" y="50" width="24" height="110" fill="var(--green)"/><text x="159" y="46">600</text>
      <rect x="214" y="107" width="24" height="53" fill="var(--navy)"/><text x="226" y="103">290</text>
      <rect x="242" y="114" width="24" height="46" fill="var(--green)"/><text x="254" y="110">250</text>
      <rect x="309" y="123" width="24" height="37" fill="var(--navy)"/><text x="321" y="119">200</text>
      <rect x="337" y="142" width="24" height="18" fill="var(--green)"/><text x="349" y="138">100</text>
    </g>
    <rect x="0" y="160" width="388" height="60" fill="var(--khaki)"/>
    <g fill="#fff" text-anchor="middle">
      <text x="50" y="176" font-size="7" font-weight="700">Asia</text>
      <text x="145" y="176" font-size="7" font-weight="700">Africa</text>
      <text x="240" y="176" font-size="7" font-weight="700">America</text>
      <text x="335" y="176" font-size="7" font-weight="700">Euro</text>
      <g font-size="4.5"><text x="50" y="185">Aut quo cum voluptatem et</text><text x="50" y="191">eos ipsum dolor sit amet velit</text>
      <text x="145" y="185">Aut quo cum voluptatem et</text><text x="145" y="191">eos ipsum dolor sit amet velit</text>
      <text x="240" y="185">Aut quo cum voluptatem et</text><text x="240" y="191">eos ipsum dolor sit amet velit</text>
      <text x="335" y="185">Aut quo cum voluptatem et</text><text x="335" y="191">eos ipsum dolor sit amet velit</text></g>
    </g>
  </svg>
</section>

<!-- 17 regions map -->
<section class="slide">
  <div class="head"><h2>Poland Map</h2><span class="brand">VelloTrack</span></div>
  <div class="photo map" style="left:14px;top:42px;width:172px;height:156px" role="img" aria-label="Map of Poland's regions with two highlighted in navy"></div>
  <p class="a" style="left:200px;top:72px;font-size:8px;font-weight:900;color:var(--navy)">BRANCHES ANALYSIS</p>
  <p class="a" style="left:200px;top:84px;font-size:20px;font-weight:900;color:var(--green)">89%</p>
  <p class="a t" style="left:245px;top:86px;width:133px">Our mission is to provide the best service and value for our customers through innovation.</p>
  <p class="a t" style="left:200px;top:112px;width:178px">Lorem ipsum dolor sit amet, consectetur adipiscing elit, sed do eiusmod tempor incididunt ut labore et dolore magna aliqua ut enim.</p>
  <table class="a data" style="left:200px;top:140px;width:178px">
    <tr><th>Branches</th><th>2014</th><th>2015</th><th>2016</th><th>2017</th><th style="background:var(--green)">2018</th></tr>
    <tr><td>Total revenue</td><td>12</td><td>15</td><td>22</td><td>28</td><td>34</td></tr>
  </table>
  <p class="foot">© Copyright 2019 Plivex by VelloTrack. All rights reserved.</p><span class="pg">17</span>
</section>

<!-- 18 three columns -->
<section class="slide">
  <div class="head"><h2>Three Column Description</h2><span class="brand">VelloTrack</span></div>
  <p class="a" style="left:14px;top:42px;width:300px;font-size:7px;font-weight:700;color:var(--ink);line-height:1.35">This is place for your header text. Insert your text here. Just replace this text with your own text</p>
  <div class="a" style="left:14px;top:68px;right:14px;display:grid;grid-template-columns:repeat(3,1fr);column-gap:14px">
    <div><p class="t">Lorem ipsum dolor sit amet, consectetur adipiscing elit, sed do eiusmod tempor incididunt ut labore et dolore magna aliqua. Ut enim ad minim veniam, quis nostrud exercitation ullamco laboris nisi ut aliquip ex ea commodo consequat.</p><p class="t" style="margin-top:5px">Duis aute irure dolor in reprehenderit in voluptate velit esse cillum dolore eu fugiat nulla pariatur.</p></div>
    <div><p class="t">Lorem ipsum dolor sit amet, consectetur adipiscing elit, sed do eiusmod tempor incididunt ut labore et dolore magna aliqua. Ut enim ad minim veniam, quis nostrud exercitation ullamco laboris nisi ut aliquip ex ea commodo consequat.</p><p class="t" style="margin-top:5px">Duis aute irure dolor in reprehenderit in voluptate velit esse cillum dolore eu fugiat nulla pariatur.</p></div>
    <div><p class="t">Lorem ipsum dolor sit amet, consectetur adipiscing elit, sed do eiusmod tempor incididunt ut labore et dolore magna aliqua. Ut enim ad minim veniam, quis nostrud exercitation ullamco laboris nisi ut aliquip ex ea commodo consequat.</p><p class="t" style="margin-top:5px">Duis aute irure dolor in reprehenderit in voluptate velit esse cillum dolore eu fugiat nulla pariatur.</p></div>
  </div>
  <p class="foot">© Copyright 2019 Plivex by VelloTrack. All rights reserved.</p><span class="pg">18</span>
</section>

<!-- 19 team single -->
<section class="slide">
  <div class="head"><h2>Our Team</h2><span class="brand">VelloTrack</span></div>
  <div class="photo person" style="left:165px;top:40px;width:58px;height:58px;border-radius:50%" role="img" aria-label="Portrait photo of the CEO"></div>
  <div class="a" style="left:104px;top:104px;width:180px;text-align:center">
    <p class="h" style="font-weight:400">Mr. John Smalley</p>
    <p style="font-size:6px;font-weight:700;color:var(--red)">CEO</p>
    <p class="t" style="margin-top:3px">Lorem ipsum dolor sit amet, consectetur adipiscing elit, sed do eiusmod tempor incididunt ut labore et dolore magna aliqua. Ut enim ad minim veniam, quis nostrud exercitation ullamco laboris.</p>
    <div style="display:flex;gap:3px;justify-content:center;margin-top:5px"><span style="width:6px;height:6px;border-radius:50%;background:var(--navy)"></span><span style="width:6px;height:6px;border-radius:50%;background:var(--navy)"></span><span style="width:6px;height:6px;border-radius:50%;background:var(--navy)"></span><span style="width:6px;height:6px;border-radius:50%;background:var(--navy)"></span></div>
  </div>
  <p class="foot">© Copyright 2019 Plivex by VelloTrack. All rights reserved.</p><span class="pg">19</span>
</section>

<!-- 20 business plan -->
<section class="slide">
  <div class="photo road" style="inset:0" role="img" aria-label="Photo of a busy motorway at dusk"></div>
  <div class="shade" style="background:rgba(21,33,74,.55)"></div>
  <h2 class="a" style="left:0;right:0;top:10px;text-align:center;font-size:12px;font-weight:900;color:#fff">Business Plan</h2>
  <p class="a t w" style="left:40px;right:40px;top:27px;text-align:center">Lorem ipsum dolor sit amet, consectetur adipiscing elit, sed do eiusmod tempor incididunt ut labore et dolore magna aliqua. Ut enim ad minim veniam quis nostrud exercitation.</p>
  <div class="tile" style="left:34px;top:62px;width:104px;height:142px;background:rgba(29,43,92,.85);text-align:left;padding:14px 10px"><p class="price">$90<small> / month</small></p><p class="h w" style="margin:6px 0 4px;letter-spacing:1px">PACKET 1</p><p class="t w">Lorem ipsum dolor sit amet, consectetur adipiscing elit sed do eiusmod tempor incididunt ut labore.</p><div style="text-align:center"><span class="btn">Get Now</span></div></div>
  <div class="tile" style="left:142px;top:62px;width:104px;height:142px;background:rgba(74,124,34,.85);text-align:left;padding:14px 10px"><p class="price">$98<small> / month</small></p><p class="h w" style="margin:6px 0 4px;letter-spacing:1px">PACKET 2</p><p class="t w">Lorem ipsum dolor sit amet, consectetur adipiscing elit sed do eiusmod tempor incididunt ut labore.</p><div style="text-align:center"><span class="btn">Get Now</span></div></div>
  <div class="tile" style="left:250px;top:62px;width:104px;height:142px;background:rgba(29,43,92,.85);text-align:left;padding:14px 10px"><p class="price">$150<small> / month</small></p><p class="h w" style="margin:6px 0 4px;letter-spacing:1px">PACKET 3</p><p class="t w">Lorem ipsum dolor sit amet, consectetur adipiscing elit sed do eiusmod tempor incididunt ut labore.</p><div style="text-align:center"><span class="btn">Get Now</span></div></div>
</section>

<!-- 21 monthly subscription -->
<section class="slide">
  <div class="head"><h2>Monthly Subscription</h2><span class="brand">VelloTrack</span></div>
  <div class="a navy-bg" style="left:0;right:0;top:135px;bottom:0"></div>
  <div class="a" style="left:52px;top:52px;width:88px;height:140px;background:#fff;box-shadow:0 1px 4px rgba(0,0,0,.2);text-align:center">
    <div style="background:var(--navy);padding:6px 0"><p style="font-size:13px;font-weight:900;color:#fff">$300</p><p style="font-size:4px;color:#fff">per month</p></div>
    <div class="t" style="padding-top:8px;line-height:2.6">Single Edition<br>Digital Goods<br>4 Slot<br>Free Update</div>
  </div>
  <div class="a" style="left:150px;top:42px;width:88px;height:150px;background:#fff;box-shadow:0 1px 4px rgba(0,0,0,.2);text-align:center">
    <div style="background:var(--green);padding:8px 0"><p style="font-size:13px;font-weight:900;color:#fff">$900</p><p style="font-size:4px;color:#fff">per month</p></div>
    <div class="t" style="padding-top:10px;line-height:2.6">Business Edition<br>Multi Client Service<br>4 Slot<br>Free Update</div>
  </div>
  <div class="a" style="left:248px;top:52px;width:88px;height:140px;background:#fff;box-shadow:0 1px 4px rgba(0,0,0,.2);text-align:center">
    <div style="background:var(--sky);padding:6px 0"><p style="font-size:13px;font-weight:900;color:#fff">$400</p><p style="font-size:4px;color:#fff">per month</p></div>
    <div class="t" style="padding-top:8px;line-height:2.6">Single Edition<br>Multi Client Service<br>Printer<br>Free Update</div>
  </div>
</section>

<!-- 22 table -->
<section class="slide">
  <div class="head"><h2>Your Title Goes Here</h2><span class="brand">VelloTrack</span></div>
  <p class="a t" style="left:12px;top:40px;width:250px"><b>Headline</b> – Lorem ipsum dolor sit amet, consectetur adipiscing elit, sed do eiusmod tempor incididunt ut labore et dolore magna aliqua ut enim.</p>
  <table class="a data" style="left:12px;top:56px;width:364px">
    <tr><th>Loremipsum</th><th>Value</th><th>Value</th><th>Value</th><th>Value</th></tr>
    <tr><td>Loremipsum</td><td>34</td><td>45</td><td>36</td><td>56</td></tr>
    <tr><td>Loremipsum</td><td>22</td><td>45</td><td>35</td><td>36</td></tr>
    <tr><td>Loremipsum</td><td>26</td><td>31</td><td>21</td><td>24</td></tr>
    <tr><td>Loremipsum</td><td>31</td><td>62</td><td>53</td><td>45</td></tr>
    <tr><td>Loremipsum</td><td>21</td><td>25</td><td>21</td><td>32</td></tr>
    <tr><td>Loremipsum</td><td>55</td><td>44</td><td>56</td><td>67</td></tr>
    <tr><td>Loremipsum</td><td>38</td><td>46</td><td>33</td><td>32</td></tr>
    <tr><td>Loremipsum</td><td>42</td><td>29</td><td>35</td><td>41</td></tr>
    <tr><td>Loremipsum</td><td>22</td><td>30</td><td>24</td><td>30</td></tr>
  </table>
  <p class="foot">© Copyright 2019 Plivex by VelloTrack. All rights reserved.</p><span class="pg">22</span>
</section>

<!-- 23 team four -->
<section class="slide">
  <div class="head"><h2>Our Team</h2><span class="brand">VelloTrack</span></div>
  <div class="photo person" style="left:18px;top:44px;width:30px;height:30px;border-radius:50%" role="img" aria-label="Portrait photo of team member"></div>
  <div class="a" style="left:54px;top:42px;width:120px"><p class="h">Michael Doran</p><p style="font-size:4.6px;font-weight:700;color:var(--navy)">MSPORTS, MBA and CEO Ph. PM</p><p class="t">• Lorem ipsum dolor sit amet, consectetur<br>• Ut enim ad minim veniam nostrud<br>• Ut enim ad minim veniam tempor<br>• Duis aute irure dolor reprehenderit</p></div>
  <div class="photo person" style="left:200px;top:44px;width:30px;height:30px;border-radius:50%" role="img" aria-label="Portrait photo of team member"></div>
  <div class="a" style="left:236px;top:42px;width:130px"><p class="h">James Dorsey</p><p style="font-size:4.6px;font-weight:700;color:var(--yellow)">Designer</p><p style="font-size:4.6px;font-weight:700;color:var(--navy)">M.B.A</p><p class="t">• Lorem ipsum dolor sit amet, consectetur<br>• Ut enim ad minim veniam nostrud<br>• Duis aute irure dolor reprehenderit</p></div>
  <div class="photo person" style="left:18px;top:126px;width:30px;height:30px;border-radius:50%" role="img" aria-label="Portrait photo of team member"></div>
  <div class="a" style="left:54px;top:124px;width:120px"><p class="h">Jane Dowell</p><p style="font-size:4.6px;font-weight:700;color:var(--yellow)">Art Director</p><p style="font-size:4.6px;font-weight:700;color:var(--navy)">M.B.A</p><p class="t">• Lorem ipsum dolor sit amet, consectetur<br>• Ut enim ad minim veniam nostrud<br>• Ut enim ad minim veniam tempor<br>• Duis aute irure dolor reprehenderit</p></div>
  <div class="photo person" style="left:200px;top:126px;width:30px;height:30px;border-radius:50%" role="img" aria-label="Portrait photo of team member"></div>
  <div class="a" style="left:236px;top:124px;width:130px"><p class="h">John Dunmore</p><p style="font-size:4.6px;font-weight:700;color:var(--yellow)">Professor</p><p class="t">• Lorem ipsum dolor sit amet, consectetur<br>• Ut enim ad minim veniam nostrud<br>• Duis aute irure dolor reprehenderit</p></div>
  <p class="foot">© Copyright 2019 Plivex by VelloTrack. All rights reserved.</p><span class="pg">23</span>
</section>

<!-- 24 two pictures -->
<section class="slide">
  <div class="head"><h2>Two Pictures Slide</h2><span class="brand">VelloTrack</span></div>
  <div class="photo road" style="left:10px;top:40px;width:178px;height:158px" role="img" aria-label="Photo of rush-hour traffic with light trails"></div>
  <div class="photo" style="left:198px;top:40px;width:180px;height:158px" role="img" aria-label="Photo of a car's tail lights in a traffic jam"></div>
</section>

<!-- 25 sales comparison -->
<section class="slide">
  <div class="head"><h2>Sales Comparison</h2><span class="brand">VelloTrack</span></div>
  <svg class="a" style="left:0;top:30px" width="388" height="190" viewBox="0 0 388 190" font-family="Lato,sans-serif">
    <text x="90" y="18" font-size="6" font-weight="700" text-anchor="middle" fill="#444">2018 Sales</text>
    <text x="298" y="18" font-size="6" font-weight="700" text-anchor="middle" fill="#444">2019 Sales</text>
    <g fill="var(--navy)" font-size="5" font-weight="700" text-anchor="middle">
      <rect x="30" y="48" width="20" height="82"/><text x="40" y="44">43</text>
      <rect x="65" y="63" width="20" height="67"/><text x="75" y="59">35</text>
      <rect x="100" y="52" width="20" height="78"/><text x="110" y="48">41</text>
      <rect x="135" y="48" width="20" height="82"/><text x="145" y="44">43</text>
    </g>
    <g fill="var(--red)" font-size="5" font-weight="700" text-anchor="middle">
      <rect x="238" y="48" width="20" height="82"/><text x="248" y="44">43</text>
      <rect x="273" y="63" width="20" height="67"/><text x="283" y="59">35</text>
      <rect x="308" y="40" width="20" height="90"/><text x="318" y="36">47</text>
      <rect x="343" y="48" width="20" height="82"/><text x="353" y="44">43</text>
    </g>
    <g font-size="4.5" fill="#666" text-anchor="middle">
      <text x="40" y="138">2016</text><text x="75" y="138">2017</text><text x="110" y="138">2018</text><text x="145" y="138">2019</text>
      <text x="248" y="138">2016</text><text x="283" y="138">2017</text><text x="318" y="138">2018</text><text x="353" y="138">2019</text>
    </g>
    <line x1="194" y1="10" x2="194" y2="140" stroke="#bbb" stroke-dasharray="3 3"/>
    <circle cx="194" cy="75" r="12" fill="var(--green)"/>
    <text x="194" y="79" font-size="9" font-weight="900" fill="#fff" text-anchor="middle">VS</text>
    <text x="22" y="170" font-size="18" font-weight="900" fill="var(--navy)">45%</text>
    <text x="66" y="162" font-size="5" font-weight="700" fill="#444">Lorem ipsum dolor</text>
    <text x="66" y="169" font-size="4.5" fill="#666">sit amet, consectetur</text>
    <text x="230" y="170" font-size="18" font-weight="900" fill="var(--red)">68%</text>
    <text x="274" y="162" font-size="5" font-weight="700" fill="var(--red)">Lorem ipsum dolor</text>
    <text x="274" y="169" font-size="4.5" fill="#666">sit amet, consectetur</text>
  </svg>
  <p class="foot">© Copyright 2019 Plivex by VelloTrack. All rights reserved.</p><span class="pg">25</span>
</section>

<!-- 26 pie chart -->
<section class="slide">
  <div class="head"><h2>Bullet &amp; Chart Area</h2><span class="brand">VelloTrack</span></div>
  <svg class="a" style="left:30px;top:44px" width="165" height="160" viewBox="0 0 165 160" font-family="Lato,sans-serif">
    <g transform="rotate(-90 70 70)" fill="none" stroke-width="50">
      <circle cx="70" cy="70" r="25" stroke="var(--navy)" stroke-dasharray="85.68 157.08"/>
      <circle cx="70" cy="70" r="25" stroke="var(--green)" stroke-dasharray="35.70 157.08" stroke-dashoffset="-85.68"/>
      <circle cx="70" cy="70" r="25" stroke="var(--red)" stroke-dasharray="21.42 157.08" stroke-dashoffset="-121.38"/>
      <circle cx="70" cy="70" r="25" stroke="var(--yellow)" stroke-dasharray="14.28 157.08" stroke-dashoffset="-142.80"/>
    </g>
    <g font-size="9" font-weight="700">
      <text x="126" y="76" fill="var(--navy)">60%</text>
      <text x="0" y="108" fill="var(--green)">25%</text>
      <text x="0" y="50" fill="var(--red)">15%</text>
      <text x="42" y="15" fill="var(--yellow)">10%</text>
    </g>
    <g font-size="4" fill="#666"><rect x="26" y="148" width="4" height="4" fill="var(--navy)"/><text x="32" y="152">1st Qtr</text><rect x="52" y="148" width="4" height="4" fill="var(--green)"/><text x="58" y="152">2nd Qtr</text><rect x="78" y="148" width="4" height="4" fill="var(--red)"/><text x="84" y="152">3rd Qtr</text><rect x="104" y="148" width="4" height="4" fill="var(--yellow)"/><text x="110" y="152">4th Qtr</text></g>
  </svg>
  <div class="a" style="left:222px;top:52px;width:150px;display:grid;row-gap:11px">
    <div class="row"><span class="ic navy" style="width:14px;height:14px;flex:none"><svg viewBox="0 0 12 12"><path d="M3 6l2 2 4-5" stroke="#fff" stroke-width="1.6" fill="none"/></svg></span><div><p class="cat" style="color:var(--navy)">Category One</p><p class="t">Lorem ipsum dolor sit amet, consectetur adipiscing elit sed do.</p></div></div>
    <div class="row"><span class="ic" style="width:14px;height:14px;flex:none"><svg viewBox="0 0 12 12"><path d="M3 6l2 2 4-5" stroke="#fff" stroke-width="1.6" fill="none"/></svg></span><div><p class="cat" style="color:var(--green)">Category Two</p><p class="t">Lorem ipsum dolor sit amet, consectetur adipiscing elit sed do.</p></div></div>
    <div class="row"><span class="ic red" style="width:14px;height:14px;flex:none"><svg viewBox="0 0 12 12"><path d="M3 6l2 2 4-5" stroke="#fff" stroke-width="1.6" fill="none"/></svg></span><div><p class="cat" style="color:var(--red)">Category Three</p><p class="t">Lorem ipsum dolor sit amet, consectetur adipiscing elit sed do.</p></div></div>
    <div class="row"><span class="ic yellow" style="width:14px;height:14px;flex:none"><svg viewBox="0 0 12 12"><path d="M3 6l2 2 4-5" stroke="#fff" stroke-width="1.6" fill="none"/></svg></span><div><p class="cat" style="color:var(--yellow)">Category Four</p><p class="t">Lorem ipsum dolor sit amet, consectetur adipiscing elit sed do.</p></div></div>
  </div>
  <p class="foot">© Copyright 2019 Plivex by VelloTrack. All rights reserved.</p><span class="pg">26</span>
</section>

<!-- 27 bar chart -->
<section class="slide">
  <div class="head"><h2>Bullet &amp; Chart Area</h2><span class="brand">VelloTrack</span></div>
  <svg class="a" style="left:10px;top:44px" width="190" height="160" viewBox="0 0 190 160" font-family="Lato,sans-serif">
    <g stroke="#e3e3e3"><line x1="40" y1="4" x2="40" y2="140"/><line x1="80" y1="4" x2="80" y2="140"/><line x1="120" y1="4" x2="120" y2="140"/><line x1="160" y1="4" x2="160" y2="140"/></g>
    <g font-size="4.5" fill="#666" text-anchor="end"><text x="36" y="24">Category 4</text><text x="36" y="58">Category 3</text><text x="36" y="92">Category 2</text><text x="36" y="126">Category 1</text></g>
    <rect x="40" y="14" width="120" height="5" fill="var(--navy)"/><rect x="40" y="20" width="80" height="5" fill="var(--red)"/><rect x="40" y="26" width="104" height="5" fill="var(--green)"/>
    <rect x="40" y="48" width="86" height="5" fill="var(--navy)"/><rect x="40" y="54" width="110" height="5" fill="var(--red)"/><rect x="40" y="60" width="60" height="5" fill="var(--green)"/>
    <rect x="40" y="82" width="98" height="5" fill="var(--navy)"/><rect x="40" y="88" width="54" height="5" fill="var(--red)"/><rect x="40" y="94" width="76" height="5" fill="var(--green)"/>
    <rect x="40" y="116" width="130" height="5" fill="var(--navy)"/><rect x="40" y="122" width="92" height="5" fill="var(--red)"/><rect x="40" y="128" width="66" height="5" fill="var(--green)"/>
    <g font-size="4" fill="#666"><rect x="60" y="150" width="4" height="4" fill="var(--navy)"/><text x="66" y="154">Series 1</text><rect x="92" y="150" width="4" height="4" fill="var(--red)"/><text x="98" y="154">Series 2</text><rect x="124" y="150" width="4" height="4" fill="var(--green)"/><text x="130" y="154">Series 3</text></g>
  </svg>
  <div class="a" style="left:222px;top:52px;width:150px;display:grid;row-gap:11px">
    <div class="row"><span class="ic navy" style="width:14px;height:14px;flex:none"><svg viewBox="0 0 12 12"><path d="M3 6l2 2 4-5" stroke="#fff" stroke-width="1.6" fill="none"/></svg></span><div><p class="cat" style="color:var(--navy)">Category One</p><p class="t">Lorem ipsum dolor sit amet, consectetur adipiscing elit sed do.</p></div></div>
    <div class="row"><span class="ic" style="width:14px;height:14px;flex:none"><svg viewBox="0 0 12 12"><path d="M3 6l2 2 4-5" stroke="#fff" stroke-width="1.6" fill="none"/></svg></span><div><p class="cat" style="color:var(--green)">Category Two</p><p class="t">Lorem ipsum dolor sit amet, consectetur adipiscing elit sed do.</p></div></div>
    <div class="row"><span class="ic red" style="width:14px;height:14px;flex:none"><svg viewBox="0 0 12 12"><path d="M3 6l2 2 4-5" stroke="#fff" stroke-width="1.6" fill="none"/></svg></span><div><p class="cat" style="color:var(--red)">Category Three</p><p class="t">Lorem ipsum dolor sit amet, consectetur adipiscing elit sed do.</p></div></div>
    <div class="row"><span class="ic yellow" style="width:14px;height:14px;flex:none"><svg viewBox="0 0 12 12"><path d="M3 6l2 2 4-5" stroke="#fff" stroke-width="1.6" fill="none"/></svg></span><div><p class="cat" style="color:var(--yellow)">Category Four</p><p class="t">Lorem ipsum dolor sit amet, consectetur adipiscing elit sed do.</p></div></div>
  </div>
  <p class="foot">© Copyright 2019 Plivex by VelloTrack. All rights reserved.</p><span class="pg">27</span>
</section>

</main>
</body>
</html>
```